New Concrete Business Requires Professional Looking Stationary

We are new business that has recently been established in Western Australia. We require a professional looking stationary suite that incorporates our new logo.

We provide concreting and construction services to commercial and private customers. This includes, ground slabs, retaining walls and other construction services.

Our new stationary should convey to our clients that they are dealing with a professional company and can depend on our reliability and strength.

Target Market(s)

Business clientèle as well as domestic clients.

Industry/Entity Type

Business

Colors
0792cd
ffffff
000000

Requirements
Must have
• The new logo and the details posted in comments section.

```html
<!DOCTYPE html>
<html lang="en">
<head>
<meta charset="utf-8">
<title>Brennan Concrete – Stationery Suite</title>
<link rel="stylesheet" href="https://fonts.googleapis.com/css2?family=Ubuntu:ital,wght@0,400;0,500;1,400&display=swap">
<style>
  :root {
    --board: #d9d9d9;
    --paper: #ffffff;
    --teal: #389fb4;
    --teal-text: #2fa1b7;
    --ink: #5a6b72;
    --grey-text: #8a8f92;
    --tint: rgba(56, 159, 180, 0.05);
    --rule: #c9d6da;
    --shadow: 0 1px 3px rgba(0,0,0,0.18);
  }
  * { box-sizing: border-box; margin: 0; padding: 0; }
  html, body { width: 1200px; height: 783px; overflow: hidden; }
  body {
    background: var(--board);
    font-family: "Ubuntu", Arial, sans-serif;
    position: relative;
  }
  .sheet {
    position: absolute;
    background: var(--paper);
    box-shadow: var(--shadow);
    overflow: hidden;
  }
  .tint-circle {
    position: absolute;
    border-radius: 50%;
    background: var(--tint);
  }
  .brand {
    position: absolute;
    display: flex;
    align-items: center;
    gap: 5px;
    color: var(--teal-text);
    font-weight: 400;
    letter-spacing: 0.03em;
    white-space: nowrap;
    line-height: 1;
  }
  .brand-mark {
    background: var(--teal);
    display: inline-block;
    flex: none;
  }
  .contact {
    position: absolute;
    color: var(--teal-text);
    text-transform: uppercase;
    font-size: 6.8px;
    line-height: 1.6;
    white-space: nowrap;
    padding-left: 10px;
    border-left: 1px solid var(--rule);
  }

  /* Letterhead */
  .letterhead { left: 27px; top: 21px; width: 522px; height: 739px; }
  .letterhead .tab { position: absolute; top: 27px; width: 6px; height: 46px; background: var(--teal); }
  .letterhead .tab-left { left: 0; }
  .letterhead .tab-right { right: 0; }
  .letterhead .brand { left: 22px; top: 58px; font-size: 12px; }
  .letterhead .brand-mark { width: 10px; height: 10px; }
  .letterhead .contact { top: 43px; }
  .letterhead .contact-address { left: 162px; }
  .letterhead .contact-web { left: 352px; }

  /* Compliments slip */
  .compliments { left: 588px; top: 21px; width: 584px; height: 276px; }
  .compliments .heading {
    position: absolute; left: 25px; top: 27px;
    font-style: italic; font-size: 11px; color: var(--grey-text); letter-spacing: 0.04em;
  }
  .compliments .brand { right: 19px; top: 45px; font-size: 11px; }
  .compliments .brand-mark { width: 8px; height: 8px; }
  .compliments .footer-band {
    position: absolute; left: 0; right: 0; bottom: 0; height: 14px;
    background: var(--teal); color: #fff; font-size: 6.2px; text-transform: uppercase;
    display: flex; align-items: center; justify-content: flex-end; padding-right: 10px;
    white-space: nowrap; overflow: hidden; gap: 8px;
  }

  /* Business cards */
  .card-front { left: 364px; top: 226px; width: 318px; height: 185px; background: var(--teal); }
  .card-front .brand { left: 0; right: 0; top: 95px; justify-content: center; color: #fff; font-size: 10.5px; }
  .card-front .brand-mark { width: 8px; height: 8px; background: #fff; }
  .card-back { left: 409px; top: 359px; width: 318px; height: 185px; }
  .card-back .brand { left: 0; right: 0; top: 59px; justify-content: center; font-size: 9px; }
  .card-back .brand-mark { width: 7px; height: 7px; }
  .card-back .details {
    position: absolute; left: 95px; top: 91px;
    border-left: 2px solid var(--teal); padding-left: 5px;
    font-size: 6.4px; line-height: 1.6; color: var(--ink); white-space: nowrap;
  }
  .card-back .details b { color: var(--teal-text); font-weight: 500; }

  /* Envelope */
  .envelope { left: 606px; top: 520px; width: 567px; height: 238px; }
  .envelope .brand { left: 38px; top: 199px; font-size: 12px; }
  .envelope .brand-mark { width: 10px; height: 10px; }
  .envelope .contact { top: 183px; }
  .envelope .contact-address { left: 185px; }
  .envelope .contact-web { left: 372px; }
</style>
</head>
<body>

<section class="sheet letterhead" aria-label="Letterhead">
  <div class="tint-circle" style="left:18px; top:-60px; width:260px; height:300px;"></div>
  <span class="tab tab-left"></span>
  <span class="tab tab-right"></span>
  <div class="brand"><span class="brand-mark"></span>BRENNAN CONCRETE</div>
  <div class="contact contact-address">Address: PO Box 218 Kelmscott WA, 6991<br>Phone: 08 9400 2750</div>
  <div class="contact contact-web">Web: www.brennanconcrete.com.au<br>Email: info@brennanconcrete.com.au<br>Brennan Pty Ltd (ACN: 612 305 478)</div>
</section>

<section class="sheet compliments" aria-label="Compliments slip">
  <div class="tint-circle" style="left:280px; top:80px; width:460px; height:460px;"></div>
  <p class="heading">WITH COMPLIMENTS</p>
  <div class="brand"><span class="brand-mark"></span>BRENNAN CONCRETE</div>
  <div class="footer-band">
    <span>Address: PO Box 218 Kelmscott WA, 6991</span><span>·</span>
    <span>Phone: 08 9400 2750</span><span>·</span>
    <span>Web: www.brennanconcrete.com.au</span><span>·</span>
    <span>Email: info@brennanconcrete.com.au</span><span>·</span>
    <span>Brennan Pty Ltd (ACN: 612 305 478)</span>
  </div>
</section>

<section class="sheet card-front" aria-label="Business card front">
  <div class="brand"><span class="brand-mark"></span>BRENNAN CONCRETE</div>
</section>

<section class="sheet card-back" aria-label="Business card back">
  <div class="tint-circle" style="left:30px; top:-20px; width:320px; height:320px;"></div>
  <div class="brand"><span class="brand-mark"></span>BRENNAN CONCRETE</div>
  <div class="details">
    <b>Address:</b> PO Box 218 Kelmscott WA, 6991<br>
    <b>Phone:</b> 08 9400 2750<br>
    <b>web:</b> www.brennanconcrete.com.au<br>
    <b>email:</b> info@brennanconcrete.com.au<br>
    <b>Brennan Pty Ltd (ACN: 612 305 478)</b>
  </div>
</section>

<section class="sheet envelope" aria-label="DL envelope">
  <div class="tint-circle" style="left:0; top:20px; width:320px; height:360px;"></div>
  <div class="brand"><span class="brand-mark"></span>BRENNAN CONCRETE</div>
  <div class="contact contact-address">Address: PO Box 218 Kelmscott WA, 6991<br>Phone: 08 9400 2750</div>
  <div class="contact contact-web">Web: www.brennanconcrete.com.au<br>Email: info@brennanconcrete.com.au<br>Brennan Pty Ltd (ACN: 612 305 478)</div>
</section>

</body>
</html>
```